Design for 3.31” x 84” vinyl banner for tradeshow

Hello, I am looking for a design that will be printed on a 33.31” x 84” vinyl banner for my company’s tradeshow booth.

-Design

My vision: I want to give you the full background, because I think it’ll help. We design insulation for electronic tools that go in high temperature oilwells. Interestingly, a lot of the electronic tools that go down these oil wells are also used in geothermal wells. However the electronics would melt in these high temperature geothermal wells if they were not insulated. A lot of companies that make tools for the oil market are trying to re-purpose their existing tools for the geothermal market…..and to do this, they would need our insulation.

So, our sign needs to conveys this message: Trying to enter the geothermal logging market? it's as simple as increasing the temp. rating for your existing tools

This sign will be placed at our company’s booth at an industry tradeshow. The sign needs to have a similar style to our existing signs. I’ve included images of our booth and all of our other signs. This sign doesn’t have to be identical in artistic style, but be fairly similar.

-Art Requirements:

At least 1 Image of RBT logo

I’ve included several different variations. Use your judgement to select the one that you think is most fitting.

Do not use the portion of the logo that says “40 years”. Feel free to crop that out if you would like.

At least 2 images of logging tools. You can select more than 2 if you think that’s necessary. Logging tools are the long metal tubes.

I’ve included several pictures of different logging tools. I would like to see at least 2 pictures of tools on the banner. Please include the image titled “Full, double centarlizer” It could look cool if this picture extended the full length of the banner (just a suggestion). I purchased these images off of picvaultly.For the second image of the tool, feel free to include whatever tool you think looks best.

-Colors and font: Like I mentioned above, I would like it to look close to the other signs we have at our booth. Please select colors and fonts that will fit with our other signs.

-Other thoughts/suggestions

When most people in our industry think of geothermal, the automatically associate it with extremely high temperatures. I’m open to seeing warmer colors (orange/red) that help convey this idea.

I’m also open to seeing pictures of geothermal power plants, I included an image of this titled “geothermal” that you may use if you like. This is not mandatory, just a suggestion.

-Text: the main text needs to be: “Trying to enter the Geothermal logging market? Ask us about increasing the temperature rating for your existing tools” No other text is required.

Printing/Art specifications:

I’ll be giving the design I receive off art-huddle to a local banner printing shop. I’ve included their printing and art guidelines, please take a look at it and let me know if you have any questions. It’s pretty detailed so I hope it provides you with enough information. The design would have to follow the requirements in the two attached word documents.

Target Market(s)

oil and gas professionals

Industry/Entity Type

oil and gas/geothermal

Font styles to use
Other font styles liked:
• Fonts similar the font used on our other tradeshow signs (images attached)

Colors
F0912C
F2A743
F7CA91
FBE8D2
FDF5EE

Requirements
Must have
• -At least 1 Image of RBT logo, At least 2 images of logging tools (1 of these 2 pictures must be image titled "full double centralizer", he main text needs to be: “Trying to enter the Geothermal logging market? Ask us about increasing the temperature rating for your existing tools” , the design must follow the requirements in the printing and art guideline documents I attached.
Nice to have
• please select colors and fonts that will fit with our other signs.

```html
<!DOCTYPE html>
<html lang="en">
<head>
<meta charset="utf-8">
<title>Geothermal Logging Banner – Redline Borehole Tech</title>
<link rel="stylesheet" href="https://fonts.googleapis.com/css2?family=Bebas+Neue&family=Open+Sans:wght@700;800&display=swap">
<style>
  :root {
    --ink: #1c1c1a;
    --orange: #ec7a1c;
    --orange-deep: #e8591a;
    --paper: #ffffff;
    --stage: #d9d9d9;
    --photo-a: #eceae6;
    --photo-b: #b9b4ab;
  }
  * { margin: 0; padding: 0; box-sizing: border-box; }
  html, body { width: 854px; height: 1200px; overflow: hidden; }
  body {
    background: var(--stage);
    font-family: "Open Sans", Arial, sans-serif;
    position: relative;
  }
  .banner {
    position: absolute;
    left: 207px; top: 45px;
    width: 440px; height: 1110px;
    background: var(--paper);
    box-shadow: 0 12px 30px rgba(0,0,0,.35);
    overflow: hidden;
  }
  .banner__header {
    position: absolute; left: 0; top: 0;
    width: 100%; height: 231px;
    background: var(--ink);
    text-align: center;
    color: var(--paper);
  }
  .header__kicker {
    position: absolute; top: 74px; width: 100%;
    font-weight: 700; font-size: 27px; letter-spacing: .5px;
    display: flex; justify-content: center; align-items: center; gap: 6px;
  }
  .dash-mark { display: inline-flex; flex-direction: column; gap: 4px; }
  .dash-mark span { display: block; width: 18px; height: 2px; background: var(--orange); }
  .header__headline {
    position: absolute; top: 112px; width: 100%;
    font-family: "Bebas Neue", Impact, sans-serif;
    font-size: 64px; line-height: 1; letter-spacing: .5px;
    color: var(--orange-deep);
  }
  .header__tail {
    position: absolute; top: 170px; width: 100%;
    font-weight: 700; font-size: 27px; letter-spacing: .5px;
  }
  .banner__photo {
    position: absolute; left: 30px; top: 248px;
    width: 398px; height: 380px;
    background: radial-gradient(ellipse at 50% 50%, var(--photo-a) 0%, var(--paper) 75%);
  }
  .banner__photo svg { width: 100%; height: 100%; display: block; }
  .ask-tab {
    position: absolute; left: 54px; top: 627px;
    width: 170px; height: 46px;
  }
  .ask-tab svg { position: absolute; inset: 0; }
  .ask-tab span {
    position: absolute; left: 18px; top: 5px;
    font-family: "Bebas Neue", Impact, sans-serif;
    font-size: 40px; line-height: 1; color: var(--paper);
  }
  .rule {
    position: absolute; left: 54px; width: 350px; height: 2px;
    background: var(--orange);
  }
  .rule--top { top: 672px; }
  .rule--bottom { top: 790px; }
  .ask-copy {
    position: absolute; left: 52px; top: 690px; width: 360px;
    font-weight: 700; font-size: 25.5px; line-height: 31px;
    color: var(--ink);
  }
  .brand {
    position: absolute; left: 40px; top: 814px;
    width: 370px; height: 104px;
    display: flex; align-items: center; gap: 14px;
  }
  .brand .dash-mark span { width: 20px; height: 2.5px; }
  .brand__square {
    width: 80px; height: 80px; background: var(--ink); flex: none;
  }
  .brand__name {
    font-weight: 800; font-size: 27px; line-height: 30px;
    color: var(--ink);
  }
  .banner__url {
    position: absolute; left: 0; top: 942px;
    width: 100%; height: 73px;
    background: var(--orange);
    color: var(--paper);
    font-weight: 800; font-size: 29px;
    display: flex; align-items: center; justify-content: center;
  }
  .banner__foot {
    position: absolute; left: 0; top: 1015px;
    width: 100%; height: 95px;
    background: var(--ink);
  }
</style>
</head>
<body>
  <main class="banner">
    <header class="banner__header">
      <p class="header__kicker">
        <span class="dash-mark"><span></span><span></span><span></span></span>
        TRYING TO ENTER
        <span class="dash-mark"><span></span><span></span><span></span></span>
      </p>
      <h1 class="header__headline">THE GEOTHERMAL</h1>
      <p class="header__tail">LOGGING MARKET?</p>
    </header>

    <div class="banner__photo" role="img" aria-label="Photograph of two downhole logging tools with centralizer arms, set diagonally">
      <svg viewBox="0 0 398 380" preserveAspectRatio="none" aria-hidden="true">
        <defs>
          <linearGradient id="toolTone" x1="0" y1="0" x2="1" y2="1">
            <stop offset="0" stop-color="var(--photo-a)"/>
            <stop offset="1" stop-color="var(--photo-b)"/>
          </linearGradient>
        </defs>
        <rect width="398" height="380" fill="url(#toolTone)" opacity=".55"/>
      </svg>
    </div>

    <div class="ask-tab">
      <svg viewBox="0 0 170 46" width="170" height="46" aria-hidden="true">
        <polygon points="0,0 144,0 170,46 0,46" fill="var(--orange)"/>
      </svg>
      <span>ASK US</span>
    </div>
    <div class="rule rule--top"></div>
    <p class="ask-copy">ABOUT THE TEMPERATURE<br>RATING FOR YOUR<br>EXISTING TOOLS</p>
    <div class="rule rule--bottom"></div>

    <div class="brand">
      <span class="dash-mark"><span></span><span></span><span></span></span>
      <span class="brand__square"></span>
      <p class="brand__name">REDLINE<br>BOREHOLE<br>TECH, Inc.</p>
    </div>

    <div class="banner__url">redlineboretech.com</div>
    <div class="banner__foot"></div>
  </main>
</body>
</html>
```